business card, stationary, return address labels

acupuncture practice in private setting...www.needlecalmstudio.example.Hope for improvement in card design, especially background and arrangement of logo.Thank you,Patricia Heraghty203.297.5399

Business

Please see attached business card

```html
<!DOCTYPE html>
<html lang="en">
<head>
<meta charset="utf-8">
<title>Needlecalm Studio – Stationery</title>
<link href="https://fonts.googleapis.com/css2?family=Montserrat:wght@300;400;600;700&display=swap" rel="stylesheet">
<style>
  :root {
    --paper: #ffffff;
    --band: #d9c8bf;
    --brown: #7a4a2a;
    --tan: #d2a66c;
    --ink: #2b211c;
    --grey: #8a7f79;
    --accent: #e03a3e;
  }
  html, body {
    margin: 0;
    padding: 0;
    width: 1200px;
    height: 1000px;
    overflow: hidden;
    background: var(--paper);
    font-family: "Montserrat", sans-serif;
  }
  .board {
    position: relative;
    width: 1200px;
    height: 1000px;
  }
  .brand-hero {
    position: absolute;
    top: 236px;
    left: 0;
    width: 1200px;
    display: flex;
    justify-content: center;
    align-items: center;
    gap: 22px;
  }
  .brand-dot {
    width: 34px;
    height: 34px;
    border-radius: 50%;
    background: var(--accent);
  }
  .brand-name {
    font-weight: 700;
    font-size: 76px;
    letter-spacing: -2px;
    color: var(--brown);
    line-height: 1;
  }
  .band {
    position: absolute;
    top: 483px;
    left: 0;
    width: 1200px;
    height: 455px;
    background: var(--band);
  }
  .card {
    position: absolute;
    top: 570px;
    width: 476px;
    height: 290px;
    background: var(--paper);
    box-shadow: 6px 7px 8px rgba(60, 40, 30, 0.35);
    box-sizing: border-box;
    overflow: hidden;
  }
  .card--contact { left: 106px; padding: 30px 22px; }
  .card--services { left: 628px; padding: 26px 16px 0 17px; }

  .contact-name {
    font-size: 15px;
    font-weight: 700;
    color: var(--brown);
    margin: 0;
  }
  .contact-name .credentials {
    font-weight: 300;
    color: var(--grey);
    margin-left: 6px;
  }
  .contact-line {
    font-size: 13px;
    font-weight: 400;
    color: var(--ink);
    margin: 0;
    line-height: 19px;
  }
  .contact-group { margin-top: 20px; }
  .contact-line .label { font-weight: 700; color: var(--brown); }
  .card-brand {
    position: absolute;
    right: 22px;
    bottom: 40px;
    font-size: 22px;
    font-weight: 700;
    letter-spacing: -0.5px;
    color: var(--brown);
  }
  .services-name {
    font-size: 34px;
    font-weight: 300;
    letter-spacing: 0.5px;
    text-transform: uppercase;
    color: var(--ink);
    margin: 0 0 14px;
    line-height: 1.1;
    white-space: nowrap;
  }
  .services-list { margin: 0; }
  .services-row {
    font-size: 12.6px;
    line-height: 18px;
    text-align: justify;
    text-align-last: justify;
    color: var(--ink);
    white-space: nowrap;
  }
  .services-row .soft { color: var(--tan); }
  .services-web {
    position: absolute;
    left: 0;
    width: 100%;
    bottom: 18px;
    text-align: center;
    font-size: 12px;
    color: var(--ink);
  }
</style>
</head>
<body>
<main class="board">
  <header class="brand-hero">
    <span class="brand-dot"></span>
    <span class="brand-name">needlecalm studio</span>
  </header>

  <section class="band"></section>

  <article class="card card--contact">
    <p class="contact-name">Rosalind Mebberton,<span class="credentials">LAc., O.T.</span></p>
    <p class="contact-line">rosalind@needlecalmstudio.example</p>
    <div class="contact-group">
      <p class="contact-line"><span class="label">t</span> 418. 563. 0827</p>
      <p class="contact-line">needlecalmstudio.example</p>
    </div>
    <div class="contact-group">
      <p class="contact-line">48B Orchard Hill Road,</p>
      <p class="contact-line">Linmere,&nbsp; CT 06599</p>
    </div>
    <div class="card-brand">needlecalm studio</div>
  </article>

  <article class="card card--services">
    <h2 class="services-name">Rosalind Mebberton</h2>
    <div class="services-list">
      <div class="services-row"><span class="soft">acute &amp; chronic</span> pain musculoskeletal <span class="soft">neurological disorders</span></div>
      <div class="services-row">diabetes &amp; neuropathy <span class="soft">circulatory conditions</span> arthritis <span class="soft">whiplash</span></div>
      <div class="services-row"><span class="soft">concussion</span> headaches &amp; migraines <span class="soft">respiratory disorders</span> anxiety</div>
      <div class="services-row"><span class="soft">insomnia</span> depression <span class="soft">stress</span> addictions <span class="soft">autoimmune conditions</span></div>
      <div class="services-row">gastrointestinal disorders <span class="soft">gynecological &amp; genitourinary disorders</span></div>
      <div class="services-row">chemotherapy and radiation side effects <span class="soft">infertility</span> morning <span class="soft">sickness</span></div>
    </div>
    <div class="services-web">www.needlecalmstudio.example</div>
  </article>
</main>
</body>
</html>
```